Valtrin Global Wordpress website design

We need a worddpress website/theme design for a new outsourcing company based in Australia.Name of the company is "Valtrin".
Website content is in progress.
The design needs to be clean without clutter in any section. Some example websites are provided below
Menu
- Resources
- Services
- Our difference
Home page needs to have a gif image, for example http://www.brelvana.com. or http://www.qorthello.com or http://www.qorthello.com/team.html
We like how the qorthello website flows without having the need to click on the menu. It is also mobile friendly (which is important)
Each piece of content will have a learn more button
A call to action button will be placed on the home page, which will provide our phone number and access to online form*
A call to action button will also be added to various other pages such as Resources.
Resources Section will contain web articles, whitepapers, blog and any other ccontent which helps customer in making a decision
Having the ability to add a video or images on the home page is also important
Ability to edit the content easily via wordpress is extremely important
* This is a great Contact Us form - http://www.lumtasko.com/#/schedule-meeting
* We do not need the traditional web form on the contact us page
Target Market(s)
Small to medium businesses requiring outsourcing services
Industry/Entity Type
It Company
Coding
Coded - Design and coding required
Colors
Designer to choose colors to be used in the design.
Look and feel

```html
<!DOCTYPE html>
<html lang="en">
<head>
<meta charset="utf-8">
<title>Valtrin Global — Home</title>
<link rel="stylesheet" href="https://fonts.googleapis.com/css2?family=Montserrat:wght@400&family=Open+Sans:wght@400;600;700&display=swap">
<style>
  :root {
    --ink-dark: #121212;
    --ink-mid: #242424;
    --ink-soft: #2e2e2e;
    --text-light: #ffffff;
    --text-muted: #d6d6d6;
    --accent-red: #ee3238;
  }
  * { margin: 0; padding: 0; box-sizing: border-box; }
  html, body {
    width: 1200px;
    height: 523px;
    overflow: hidden;
    background: var(--ink-dark);
    font-family: "Open Sans", Arial, sans-serif;
  }
  .hero {
    position: relative;
    width: 1200px;
    height: 523px;
    overflow: hidden;
  }
  .hero-backdrop {
    position: absolute;
    inset: 0;
    background:
      radial-gradient(ellipse 420px 260px at 760px 170px, rgba(70,70,70,0.55), transparent 70%),
      radial-gradient(ellipse 360px 220px at 1050px 200px, rgba(60,60,60,0.45), transparent 70%),
      radial-gradient(ellipse 300px 200px at 330px 160px, rgba(55,55,55,0.4), transparent 70%),
      linear-gradient(180deg, var(--ink-soft) 0%, var(--ink-mid) 45%, var(--ink-dark) 100%);
  }
  .site-header {
    position: absolute;
    top: 0;
    left: 0;
    right: 0;
    height: 72px;
  }
  .brand {
    position: absolute;
    left: 122px;
    top: 14px;
    font-family: "Montserrat", "Open Sans", sans-serif;
    font-weight: 400;
    font-size: 37px;
    letter-spacing: 4px;
    line-height: 40px;
    color: var(--text-light);
  }
  .main-nav {
    position: absolute;
    top: 27px;
    right: 114px;
    display: flex;
    align-items: center;
    gap: 21px;
    font-size: 13px;
    font-weight: 600;
    color: var(--text-muted);
  }
  .main-nav a {
    color: inherit;
    text-decoration: none;
    position: relative;
    line-height: 18px;
    white-space: nowrap;
  }
  .main-nav a.is-current { color: var(--text-light); }
  .main-nav a.is-current::after {
    content: "";
    position: absolute;
    left: 0;
    right: 0;
    bottom: -5px;
    height: 1px;
    background: var(--text-light);
  }
  .search-icon { display: block; }
  .hero-content {
    position: absolute;
    left: 120px;
    top: 197px;
    width: 460px;
    color: var(--text-light);
  }
  .hero-title {
    font-size: 34.5px;
    font-weight: 700;
    line-height: 41px;
    text-transform: uppercase;
    letter-spacing: 0.2px;
  }
  .hero-text {
    margin-top: 10px;
    font-size: 12.4px;
    line-height: 21px;
    font-weight: 400;
    width: 440px;
  }
  .hero-actions {
    display: flex;
    gap: 12px;
    margin-top: 15px;
  }
  .btn {
    display: inline-block;
    font-size: 14.5px;
    line-height: 32px;
    height: 32px;
    padding: 0 14px;
    text-transform: uppercase;
    text-decoration: none;
    color: var(--text-light);
    white-space: nowrap;
  }
  .btn-read-more { background: var(--accent-red); }
  .btn-call {
    border: 1px solid var(--text-light);
    line-height: 30px;
  }
  .scroll-cue {
    position: absolute;
    left: 595px;
    top: 486px;
  }
</style>
</head>
<body>
  <section class="hero">
    <div class="hero-backdrop" role="img" aria-label="Darkened, blurred photo of a busy office with people working by tall windows"></div>

    <header class="site-header">
      <div class="brand">VALTRIN</div>
      <nav class="main-nav">
        <a href="#" class="is-current">Home</a>
        <a href="#">Resources</a>
        <a href="#">Services</a>
        <a href="#">Our Difference</a>
        <a href="#">Contact Us</a>
        <svg class="search-icon" width="16" height="16" viewBox="0 0 16 16" aria-label="Search">
          <circle cx="9.5" cy="6.5" r="5" fill="none" stroke="#d6d6d6" stroke-width="1.4"/>
          <line x1="6" y1="10" x2="1.5" y2="14.5" stroke="#d6d6d6" stroke-width="1.5"/>
        </svg>
      </nav>
    </header>

    <div class="hero-content">
      <h1 class="hero-title">Best creative agency<br>for your needs</h1>
      <p class="hero-text">Lorem ipsum dolor sit amet, consectetur adipiscing elit. Phasellus elit dui, cursus elementum condimentum sodales, pulvinar sed nisi. Curabitur sed blandit eros. Aliquam erat volutpat.</p>
      <div class="hero-actions">
        <a href="#" class="btn btn-read-more">Read More</a>
        <a href="#" class="btn btn-call">Call 1300 555 014</a>
      </div>
    </div>

    <svg class="scroll-cue" width="12" height="8" viewBox="0 0 12 8" aria-label="Scroll down">
      <polyline points="1,1.5 6,6.5 11,1.5" fill="none" stroke="#ffffff" stroke-width="1.8"/>
    </svg>
  </section>
</body>
</html>
```